Hotel Business Card Project

Amber Crest Hotel will be a premium boutique hotel in Dhaka, Bangladesh. The hotel will offer the finest amenities and facilities available on the market, and the cost per room investment will far exceed other 5-star hotels currently in the market.

As a result, we wanted the business card to reflect that premium/luxurious/upscale feel, and also be elegant and hospitable at the same time.

The name 'Amber Crest' is derived from the fact that Bangladesh has 6 distinct seasons (you can get more information online if required, or contact me about it). The leaves in the logo has the tree because trees give people shade, protection and safety (just like our hotel would try to give).

Target Market(s)

Business professionals, guests

Industry/Entity Type

Investment

Requirements
Must have
• Elegant, Classy and very attractive business card.

Must be editable to enter specific Names, Positions, Phone numbers and email later on.
Nice to have
• The address would be: House 42, Road 57, Banani 4, Dhaka 1230, Bangladesh

Slogan- Luxury Redefined

```html
<!DOCTYPE html>
<html lang="en">
<head>
<meta charset="utf-8">
<title>Amber Crest Hotel — Business Card</title>
<link rel="stylesheet" href="https://fonts.googleapis.com/css2?family=Sorts+Mill+Goudy&display=swap">
<style>
  :root {
    --backdrop: #2e2e2e;
    --card-paper: #f4f2ec;
    --card-paper-edge: #ecE9e1;
    --ink-grey: #6f6f6f;
    --ink-dark: #4a4a4a;
    --rule-grey: #b9b7b1;
    --amber: #d9893f;
  }
  * { box-sizing: border-box; margin: 0; padding: 0; }
  html, body {
    width: 1200px;
    height: 900px;
    overflow: hidden;
    background: var(--backdrop);
  }
  .canvas {
    position: relative;
    width: 1200px;
    height: 900px;
  }
  .card {
    position: absolute;
    top: 308px;
    width: 513px;
    height: 285px;
    border-radius: 18px;
    background: radial-gradient(ellipse at 50% 40%, var(--card-paper) 60%, var(--card-paper-edge) 100%);
    box-shadow: 0 3px 8px rgba(0,0,0,0.45);
    font-family: "Sorts Mill Goudy", Georgia, serif;
    text-align: center;
  }
  .card--front { left: 73px; }
  .card--back { left: 615px; }

  .front-mark {
    position: absolute;
    left: 0; right: 0;
    top: 70px;
    display: flex;
    flex-direction: column;
    align-items: center;
    gap: 34px;
  }
  .brand-dot {
    width: 64px;
    height: 64px;
    border-radius: 50%;
    background: var(--amber);
  }
  .brand-name {
    font-size: 36px;
    color: var(--ink-grey);
    letter-spacing: 1px;
    line-height: 1;
  }

  .back-name {
    position: absolute;
    left: 0; right: 0;
    top: 38px;
    font-size: 36px;
    color: var(--ink-grey);
    letter-spacing: 1px;
    line-height: 1;
  }
  .back-slogan {
    position: absolute;
    left: 0; right: 0;
    top: 82px;
    font-size: 12px;
    color: var(--ink-grey);
    letter-spacing: 3px;
    text-transform: uppercase;
  }
  .address {
    position: absolute;
    left: 0; right: 0;
    top: 136px;
    font-size: 16px;
    line-height: 21px;
    color: var(--ink-dark);
    font-style: normal;
  }
  .divider {
    position: absolute;
    left: 145px;
    width: 225px;
    top: 218px;
    height: 1px;
    background: var(--rule-grey);
  }
  .contact {
    position: absolute;
    left: 0; right: 0;
    top: 230px;
    font-size: 12.5px;
    line-height: 16px;
    color: var(--ink-dark);
  }
</style>
</head>
<body>
  <main class="canvas">
    <section class="card card--front" aria-label="Business card front">
      <div class="front-mark">
        <span class="brand-dot" aria-hidden="true"></span>
        <h1 class="brand-name">Amber Crest Hotel</h1>
      </div>
    </section>

    <section class="card card--back" aria-label="Business card back">
      <h2 class="back-name">Amber Crest Hotel</h2>
      <p class="back-slogan">Luxury Redefined</p>
      <address class="address">
        House 42, Road 57<br>
        Banani 4, Dhaka 1230<br>
        Bangladesh
      </address>
      <div class="divider" aria-hidden="true"></div>
      <p class="contact">
        Tel.: +880 2 555 0142, fax: +880 2 555 0198<br>
        hotel@ambercrest.bg, www.ambercrest.bg
      </p>
    </section>
  </main>
</body>
</html>
```